School Auction Party Invitation- Create... the Future.

We need a logo design and invitation for our school auction fundraiser party. Our theme is Create.... The Future. We are trying to incorporate technology, creativity, 21st century learning, and make use of fun, graphic design. colors: black, white, silver, and a bright(almost neon) accent colors. (orange-primary)
Updates

Deadline update: Logo-October 23, Invite- Nov. 7

Target Market(s)

Parents of a private preschool-8th grade students from the Bay Area (majority age 40s, some 30s and 50s) All passionate about kids, education, some varying backgrounds/incomes, but majority upper class-educated. annual school auction/fundraiser. want to create interest/excitement- fun community party. we are trying to focus the theme on creativity & the future (technology, our kid's futures, etc)
www.morvendale.org

Industry/Entity Type

School

Requirements
Must have
• Logo file, One page invite (5x7 including date, time, place, rsvp info, need digital file to print locally

add band logo (possibly tie in to invite look) www.quietharborkitesband.com
Nice to have
• fun, creative, futuristic, abstract, sleek, graphic art. we will be using LED & glow lights at fundraiser
Should not have
• pictures of people

```html
<!DOCTYPE html>
<html lang="en">
<head>
<meta charset="utf-8">
<title>The Morvendale School Annual Auction Gala Invitation</title>
<link rel="stylesheet" href="https://fonts.googleapis.com/css2?family=Audiowide&family=Aldrich&family=Open+Sans:wght@400;600;700&display=swap">
<style>
  :root {
    --page-bg: #d9d9d9;
    --card-black: #050505;
    --white: #ffffff;
    --neon-orange: #ff9a1a;
    --neon-gold: #ffc93c;
    --neon-magenta: #e0218a;
    --neon-violet: #7b3fd6;
    --neon-blue: #2a8cff;
    --neon-cyan: #6fe3ff;
    --note-yellow: #f7ec7a;
    --note-blue: #bfe6f7;
    --ink: #1b1b1b;
  }
  * { box-sizing: border-box; margin: 0; padding: 0; }
  html, body { width: 1200px; height: 900px; overflow: hidden; }
  body {
    background: var(--page-bg);
    position: relative;
    font-family: "Open Sans", Arial, sans-serif;
  }
  .invitation {
    position: absolute;
    left: 293px; top: 20px;
    width: 614px; height: 860px;
    background: var(--card-black);
    color: var(--white);
    overflow: hidden;
  }
  .light-burst {
    position: absolute;
    left: 0; top: 78px; width: 614px; height: 400px;
    background:
      radial-gradient(ellipse 60% 10% at 50% 50%, rgba(255,255,255,0.55), transparent 80%),
      linear-gradient(90deg, var(--neon-gold) 0%, var(--neon-orange) 14%, var(--neon-magenta) 36%, #b02ab0 50%, var(--neon-violet) 64%, var(--neon-blue) 82%, var(--neon-cyan) 100%);
    -webkit-mask-image: radial-gradient(ellipse 75% 50% at 50% 50%, #000 25%, rgba(0,0,0,0.55) 60%, transparent 100%);
            mask-image: radial-gradient(ellipse 75% 50% at 50% 50%, #000 25%, rgba(0,0,0,0.55) 60%, transparent 100%);
    opacity: 0.92;
  }
  .theme-mark {
    position: absolute;
    top: 30px; left: 0; width: 100%;
    display: flex; align-items: center; justify-content: center; gap: 12px;
  }
  .theme-mark__dot {
    width: 32px; height: 32px; border-radius: 50%;
    background: var(--neon-orange);
  }
  .theme-mark__name {
    font-family: "Audiowide", "Arial Black", sans-serif;
    font-size: 38px;
    color: var(--neon-orange);
    letter-spacing: 0.5px;
  }
  .event-title {
    position: absolute;
    top: 458px; left: 0; width: 100%;
    text-align: center;
    font-family: "Aldrich", Arial, sans-serif;
    font-weight: 400;
    line-height: 1.15;
  }
  .event-title__school { display: block; font-size: 40px; }
  .event-title__gala { display: block; font-size: 33px; }
  .event-purpose {
    position: absolute;
    top: 558px; left: 0; width: 100%;
    text-align: center;
    font-family: "Aldrich", Arial, sans-serif;
    font-size: 17px;
    line-height: 28px;
  }
  .info-card {
    position: absolute;
    top: 626px; height: 140px;
    border-radius: 20px;
    color: var(--ink);
  }
  .info-card--venue {
    left: 37px; width: 252px;
    background: var(--note-yellow);
    padding: 20px 0 0 19px;
  }
  .venue__date { font-weight: 700; font-size: 16px; margin-bottom: 14px; }
  .venue__address { font-size: 15.5px; line-height: 21px; }
  .info-card--schedule {
    left: 312px; width: 278px;
    background: var(--note-blue);
    padding: 13px 10px 0 16px;
    font-size: 12px;
    line-height: 16px;
  }
  .schedule__row { display: flex; }
  .schedule__time { font-weight: 700; white-space: nowrap; margin-right: 5px; }
  .band {
    margin-top: 9px;
    display: flex; align-items: center; gap: 6px;
  }
  .band__square { width: 11px; height: 11px; background: var(--neon-orange); }
  .band__name {
    font-size: 14px; font-weight: 600; letter-spacing: 0.5px;
    text-transform: uppercase; color: var(--ink);
  }
  .band__note { font-size: 9px; line-height: 12px; white-space: nowrap; margin-top: 1px; }
  .rsvp {
    position: absolute;
    top: 786px; left: 0; width: 100%;
    text-align: center;
    font-weight: 600;
    font-size: 16.5px;
    line-height: 24px;
  }
</style>
</head>
<body>
  <main class="invitation">
    <div class="light-burst" role="img" aria-label="Abstract glowing bokeh lights sweeping from orange through magenta to blue across a starry black space"></div>

    <header class="theme-mark">
      <span class="theme-mark__dot"></span>
      <span class="theme-mark__name">Create... The Future!</span>
    </header>

    <h1 class="event-title">
      <span class="event-title__school">The Morvendale School</span>
      <span class="event-title__gala">Annual Auction Gala</span>
    </h1>

    <p class="event-purpose">A celebration to benefit our children's bright futures<br>and to support our amazing faculty and staff</p>

    <section class="info-card info-card--venue">
      <p class="venue__date">Saturday, March 22, 2014</p>
      <p class="venue__address">Fernbrook Country Club<br>2250 Lindell Ridge Drive<br>Fernbrook, CA 94612</p>
    </section>

    <section class="info-card info-card--schedule">
      <div class="schedule__row"><span class="schedule__time">5:30 p.m.</span><span>Silent Auction, cocktails,<br>and live social time</span></div>
      <div class="schedule__row"><span class="schedule__time">7:00 p.m.</span><span>Dinner and Live Auction</span></div>
      <div class="schedule__row"><span class="schedule__time">8:00 p.m.</span><span>Live music and dancing</span></div>
      <div class="band"><span class="band__square"></span><span class="band__name">Quiet Harbor Kites</span></div>
      <p class="band__note">(Bay area band, and Morvendale parent Tom Ashby)</p>
    </section>

    <p class="rsvp">Please return the enclosed rsvp card or rsvp online by March 14<br>Take an exciting trip into the future and celebrate our community!</p>
  </main>
</body>
</html>
```